"Tarvel Mouthguards " Custom-made Mouthguard Business Website

We need an informational website for our mouthguard Business "Tarvel Mouthguards". The logo is navy blue/lime green so want to have colour scheme that goes nicely with this - have uploaded our mouthguard flyer with some information we need to put into the website but I do have more information to put in there.

Target Market(s)

Sports clubs, sportspeople, parents and kids, schools

Industry/Entity Type

Dental, Custom-made Sports Mouthguards

Coding

Number of Pages Required

5+ page

Font styles to use
Serif
Sans Serif

Colors
0054AA
0677BA
7BADD7
CADEEF
E8F1F8
0094D4
00A9DD
6FCCEA
C7EBF8
E9F6FB
00AB8E
00BBA5
67D7C9
C6EFE9
E9F9F6
59FF00
82FF00
B8FF75
E3FFCB
F4FFEA
FFF300
FFF600
FEFA6F
FFFEC7
FFFEE8
FFC000
F8CF3A
FAE287
FDF2CF
FEFAEE
F0912C
F2A743
F7CA91
FBE8D2
FDF5EE
EE7325
F08F49
F5BC92
FAE3D3
FDF4ED

Requirements
Must have
• I want drop down pages, not one scrolling page. Different pages for each heading . Content uploaded - We need a general home page with lots of pictures and info that I'll provide. A page each dedicated to 1) About Us 2) Why choose a custom mouthguard? 3) Gallery 4) Contact Us. Will need logos from "Morvex"
Nice to have
• Mainly use greens and blues, but happy to pop in some yellow/oranges/red oranges if it looks good

```html
<!DOCTYPE html>
<html lang="en">
<head>
<meta charset="utf-8">
<title>Tarvel Mouthguards</title>
<link href="https://fonts.googleapis.com/css2?family=Inter:wght@400;500;600;700;800&display=swap" rel="stylesheet">
<style>
:root{
  --navy:#0b2a66;
  --navy-deep:#08214f;
  --lime:#3fd42c;
  --ink:#0f1b33;
  --muted:#5b6475;
  --paper:#ffffff;
  --mist:#eef2f7;
  --line:#d9dee7;
}
*{box-sizing:border-box;margin:0;padding:0}
html,body{width:1200px;height:4000px;overflow:hidden}
body{font-family:"Inter",Arial,sans-serif;color:var(--ink);background:var(--paper);position:relative}
.abs{position:absolute}
.btn{display:inline-flex;align-items:center;gap:10px;background:var(--navy);color:#fff;font-weight:600;font-size:14px;padding:0 22px;height:44px;border-radius:3px;text-decoration:none}
.btn svg{width:14px;height:14px}
.sq{position:absolute}
.sq.lime{background:var(--lime)}
.sq.white{background:#fff}
.sq.navy{background:var(--navy)}
.sq.grey{background:#e4e8ee}

/* header */
.site-header{position:absolute;top:0;left:0;width:1200px;height:80px;background:#fff;display:flex;align-items:center;padding:0 110px}
.brand{display:flex;align-items:center;gap:10px;font-weight:800;font-size:19px;color:var(--navy);letter-spacing:.5px;line-height:1}
.brand .mark{width:18px;height:18px;background:var(--lime)}
.main-nav{display:flex;gap:26px;margin-left:80px;font-size:13px;color:var(--ink)}
.site-header .btn{margin-left:auto}

/* hero */
.hero{position:absolute;top:80px;left:0;width:1200px;height:400px}
.hero-photo{position:absolute;inset:0;background:linear-gradient(100deg,#3f6a3c 0%,#5c8f4a 35%,#9ab7c9 60%,#2f5fa8 100%)}
.hero-title{position:absolute;left:120px;top:150px;color:#fff;font-size:42px;font-weight:800;line-height:1.12;width:420px}
.hero .btn{position:absolute;left:120px;top:315px;height:40px}

/* about */
.about-photo{left:50px;top:510px;width:390px;height:350px;background:linear-gradient(135deg,#f4c1d9,#8fd0f0 35%,#f7d25a 60%,#b79be8 85%,#f3f3f3)}
.about-copy{left:520px;top:540px;width:600px}
.eyebrow{font-size:13px;color:var(--ink);margin-bottom:10px}
.about-copy h2{font-size:25px;font-weight:800;letter-spacing:.3px;margin-bottom:14px}
.about-copy p{font-size:13px;line-height:1.6;color:var(--muted);width:480px}
.features{display:flex;gap:28px;margin-top:28px}
.feature{width:175px}
.feature .icon{width:62px;height:62px;background:var(--navy);display:flex;align-items:center;justify-content:center;margin-bottom:18px}
.feature h3{font-size:15px;font-weight:700;margin-bottom:8px}
.feature p{font-size:11px;line-height:1.55;width:auto}

/* types */
.navy-band{left:0;top:1180px;width:1200px;height:650px;background:var(--navy)}
.showcase-photo{left:200px;top:1000px;width:860px;height:400px;background:linear-gradient(120deg,#e9eff6 0%,#cfdcec 45%,#dfe8f2 75%,#f3f6fa 100%)}
.types{left:120px;top:1540px;width:960px;color:#fff}
.types h2{font-size:40px;font-weight:600;margin-bottom:70px}
.type-list{display:flex;gap:40px}
.type{width:210px}
.type h3{color:var(--lime);font-size:22px;font-weight:600;margin-bottom:12px}
.type p{font-size:11px;line-height:1.55;color:#d6def0}

/* design options */
.design{left:120px;top:1915px;width:420px}
.design h2{font-size:40px;font-weight:700;margin-bottom:26px}
.design p{font-size:12px;line-height:1.65;color:var(--muted);margin-bottom:22px}
.design .link{font-size:12px;font-weight:700;color:var(--ink);margin-bottom:22px}
.design .btn{height:40px;margin-top:30px}
.steps{left:670px;top:1905px;width:440px}
.step{display:flex;gap:30px;height:170px}
.step .box{width:80px;height:80px;background:var(--navy);flex:none}
.step h3{font-size:16px;font-weight:600;margin:4px 0 12px}
.step p{font-size:11px;line-height:1.55;color:var(--muted)}

/* gallery */
.gallery{left:0;top:2530px;width:1200px;height:480px;background:var(--navy)}
.gallery h2{position:absolute;left:112px;top:55px;color:#fff;font-size:40px;font-weight:700}
.gallery .view-more{position:absolute;left:864px;top:58px;height:44px;background:var(--lime);color:#fff}
.shot{position:absolute;top:150px;height:330px}
.shot.a{left:112px;width:350px;background:linear-gradient(135deg,#c9d9e6,#7fa6c9 40%,#dfe7ef)}
.shot.b{left:482px;width:340px;background:linear-gradient(135deg,#f1e7dc,#c43a32 45%,#f3f3f3)}
.shot.c{left:842px;width:320px;background:linear-gradient(135deg,#d8f0f6,#a7d6e8 40%,#f0f5f8)}

/* faq */
.faq{left:0;top:3010px;width:1200px;height:510px;background:var(--mist)}
.faq h2{text-align:center;font-size:32px;font-weight:600;margin-top:70px;margin-bottom:36px}
.faq-list{width:940px;margin:0 auto}
.faq-item{background:#fff;margin-bottom:20px}
.faq-q{height:50px;display:flex;align-items:center;justify-content:space-between;padding:0 20px;font-size:14px;font-weight:500}
.faq-item.open .faq-q{background:var(--navy);color:#fff}
.faq-a{padding:16px 20px 18px;font-size:11px;color:var(--muted);line-height:1.55}
.plus{font-size:20px;font-weight:400}

/* footer */
.site-footer{left:0;top:3520px;width:1200px;height:440px;background:var(--navy);color:#fff}
.site-footer .brand{position:absolute;left:112px;top:70px;color:#fff}
.footer-about{position:absolute;left:112px;top:120px;width:320px;font-size:11px;line-height:1.6;color:#d6def0}
.socials{position:absolute;left:112px;top:195px;display:flex;gap:8px}
.socials span{width:26px;height:26px;background:var(--lime)}
.footer-col{position:absolute;top:75px}
.footer-col h4{font-size:16px;font-weight:600;margin-bottom:22px}
.footer-col li{list-style:none;font-size:12px;color:#d6def0;margin-bottom:18px}
.bottom-bar{left:0;top:3960px;width:1200px;height:40px;background:var(--lime);display:flex;align-items:center;justify-content:space-between;padding:0 112px;font-size:11px;color:var(--navy-deep)}
</style>
</head>
<body>

<header class="site-header">
  <div class="brand"><span class="mark"></span>TARVEL MOUTHGUARDS</div>
  <nav class="main-nav"><span>Home</span><span>About Us</span><span>Services</span><span>Page</span><span>Contact Us</span></nav>
  <a class="btn">Get Started <svg viewBox="0 0 14 14"><path d="M2 7h10M8 3l4 4-4 4" stroke="#fff" stroke-width="1.8" fill="none"/></svg></a>
</header>

<section class="hero">
  <div class="hero-photo" role="img" aria-label="Young athlete wearing a colourful custom mouthguard on a sports field"></div>
  <h1 class="hero-title">Protect Your Smile with a Custom Mouthguard</h1>
  <a class="btn">Get Started <svg viewBox="0 0 14 14"><path d="M2 7h10M8 3l4 4-4 4" stroke="#fff" stroke-width="1.8" fill="none"/></svg></a>
  <div class="sq white" style="left:1000px;top:260px;width:70px;height:70px;opacity:.85"></div>
  <div class="sq lime" style="left:1070px;top:330px;width:70px;height:70px"></div>
  <div class="sq white" style="left:1140px;top:260px;width:60px;height:70px;opacity:.6"></div>
  <div class="sq white" style="left:1140px;top:330px;width:60px;height:70px"></div>
</section>

<div class="abs about-photo" role="img" aria-label="Grid of colourful patterned custom mouthguards"></div>
<div class="sq lime" style="left:40px;top:800px;width:70px;height:70px"></div>
<section class="abs about-copy">
  <p class="eyebrow">About Us</p>
  <h2>WHY CHOOSE A CUSTOM MOUTHGUARD?</h2>
  <p>Not all mouthguards are created equal. Chemist-bought "boil and bite" guards might seem convenient, but they often provide poor fit and limited protection. A custom mouthguard, professionally fitted to your teeth and bite, offers:</p>
  <div class="features">
    <div class="feature">
      <div class="icon"><svg width="26" height="26" viewBox="0 0 26 26"><path d="M13 2l9 4v7c0 6-4 9-9 11-5-2-9-5-9-11V6z" fill="none" stroke="#fff" stroke-width="2"/></svg></div>
      <h3>Maximum Protection</h3>
      <p>absorbs impact and helps prevent broken teeth, jaw injuries, and concussions.</p>
    </div>
    <div class="feature">
      <div class="icon"><svg width="26" height="26" viewBox="0 0 26 26"><circle cx="13" cy="13" r="10" fill="none" stroke="#fff" stroke-width="2"/><path d="M8 13l4 4 7-8" fill="none" stroke="#fff" stroke-width="2"/></svg></div>
      <h3>Superior Comfort</h3>
      <p>designed to fit snugly, making it easier to breathe and talk while playing.</p>
    </div>
    <div class="feature">
      <div class="icon"><svg width="26" height="26" viewBox="0 0 26 26"><rect x="4" y="4" width="18" height="18" fill="none" stroke="#fff" stroke-width="2"/><path d="M9 13h8M13 9v8" stroke="#fff" stroke-width="2"/></svg></div>
      <h3>Enhanced Durability</h3>
      <p>crafted from high-quality dental materials that outlast off-the-shelf options.</p>
    </div>
  </div>
</section>
<div class="sq lime" style="left:1060px;top:890px;width:50px;height:50px"></div>

<div class="abs navy-band"></div>
<div class="abs showcase-photo" role="img" aria-label="Product photo of bright multicoloured custom mouthguards and a storage case"></div>
<div class="sq lime" style="left:1045px;top:1150px;width:70px;height:70px"></div>
<div class="sq white" style="left:120px;top:1340px;width:80px;height:80px"></div>
<div class="sq navy" style="left:975px;top:1355px;width:60px;height:60px;background:#06183d"></div>
<div class="sq grey" style="left:1130px;top:1340px;width:70px;height:70px;opacity:.25"></div>

<section class="abs types">
  <h2>Types Available</h2>
  <div class="type-list">
    <div class="type"><h3>Kid's mouthguards</h3><p>protective and comfortable for growing dentition</p></div>
    <div class="type"><h3>Single-layer</h3><p>suitable for low-medium contact sports (children generally will have a single-layer mouthguard).</p></div>
    <div class="type"><h3>Double-layer</h3><p>recommended for high-impact sports</p></div>
    <div class="type"><h3>Triple-layer</h3><p>We are able to do triple-layer mouthguards for sports that require that little bit of extra protection.</p></div>
  </div>
</section>

<section class="abs design">
  <h2>Design Options</h2>
  <p>Design your own mouthguard with a choice of nearly 40 colours which you can mix and match into different styles. Choose from team colours, stripes, marbled effects, even harlequin patterns. We can also offer glitter over any colour you choose.</p>
  <p>All of our mouthguard colours and styles are locally made, right here in WA. Take a look at the full range of colours and styles you can choose from at</p>
  <p class="link">www.tarvelguards-studio.com →</p>
  <p>If you have your colours and a style in mind before your appointment with us you are one step ahead!</p>
  <a class="btn">Book Now <svg viewBox="0 0 14 14"><path d="M2 7h10M8 3l4 4-4 4" stroke="#fff" stroke-width="1.8" fill="none"/></svg></a>
</section>

<section class="abs steps">
  <div class="step"><div class="box"></div><div><h3>Step 1</h3><p>Book an appointment or mobile visit with our dental prosthetists.</p></div></div>
  <div class="step"><div class="box"></div><div><h3>Step 2</h3><p>Impressions are taken of the mouth – this appointment will generally take around 15 minutes. You then get to choose your design (if you haven't already!)</p></div></div>
  <div class="step"><div class="box"></div><div><h3>Step 3</h3><p>Mouthguard is made in-house in our laboratory by our prosthetist and technicians.</p></div></div>
  <div class="step"><div class="box"></div><div><h3>Step 4</h3><p>Fit and collection – you may either pick up from our clinic – or for sporting clubs or schools, we can have them packed and delivered to you.</p></div></div>
</section>

<section class="abs gallery">
  <h2>Gallery</h2>
  <a class="btn view-more">View More <svg viewBox="0 0 14 14"><path d="M2 7h10M8 3l4 4-4 4" stroke="#fff" stroke-width="1.8" fill="none"/></svg></a>
  <div class="shot a" role="img" aria-label="Blue and white marbled mouthguards"></div>
  <div class="shot b" role="img" aria-label="Red and white harlequin patterned mouthguard"></div>
  <div class="shot c" role="img" aria-label="Clear glitter mouthguard with pastel colours"></div>
  <div class="sq lime" style="left:0;top:410px;width:60px;height:70px"></div>
  <div class="sq white" style="left:1140px;top:-10px;width:60px;height:60px;background:#0c1e44"></div>
</section>
<div class="sq lime" style="left:1140px;top:3015px;width:60px;height:60px"></div>

<section class="abs faq">
  <h2>Frequently Asked Questions</h2>
  <div class="faq-list">
    <div class="faq-item open">
      <div class="faq-q"><span>How long does a mouthguard last?</span><span class="plus">+</span></div>
      <div class="faq-a">1-2 years for adults. Children generally will need a new fitting each year as their teeth and size of their mouths are changing month to month.</div>
    </div>
    <div class="faq-item"><div class="faq-q"><span>Are mouthguards covered by health funds?</span><span class="plus">+</span></div></div>
    <div class="faq-item"><div class="faq-q"><span>Why not buy a mouthguard from the Chemist?</span><span class="plus">+</span></div></div>
    <div class="faq-item"><div class="faq-q"><span>Do you visit schools and clubs?</span><span class="plus">+</span></div></div>
  </div>
</section>

<footer class="abs site-footer">
  <div class="brand"><span class="mark"></span>TARVEL MOUTHGUARDS</div>
  <p class="footer-about">With over 20 years' experience in the industry, our dental prosthetists take care to provide mouthguards that are made with precision and shaped for your comfort and protection.</p>
  <div class="socials"><span></span><span></span><span></span></div>
  <div class="footer-col" style="left:605px">
    <h4>Navigation</h4>
    <ul><li>Home</li><li>About Us</li><li>Services</li><li>Contact Us</li></ul>
  </div>
  <div class="footer-col" style="left:865px">
    <h4>Resources</h4>
    <ul><li>Customer Stories</li><li>Help Center</li><li>Documentation</li><li>Blog &amp; Guide</li></ul>
  </div>
</footer>
<div class="abs bottom-bar"><span>Copyright © 2023 Tarvel Mouthguards</span><span>Terms of Use • Privacy Policy</span></div>

</body>
</html>
```